Granite Ridge College-Pinecrest Welcome Week

I am the Student Activities Coordinator at Granite Ridge College-Pinecrest. For Welcome Week 2013, I need a standard poster 24x36 with the list of events happening. Our theme is based on the popular Friday Late Laughs video "We Got a Kite"
http://www.vidtrove.example/clip/Q4mZp8sLwTe
Our theme is:
We're at the 'Crest!
Welcome Week 2013
Graphics on the poster should reflect popular images/designs of FLL We Got a Kite. However, the boat should be a steamboat instead of the yacht image.
Unfortunately, I have a lot of text to fit on the poster. Traditionally we go with 3 margins listing events. I'm attaching the word document of events and our logo to this proposal. I'll also attach a few google images of "We Got a Kite" that align with the type of theme I'm looking for.
One last thing, our logo contains mountains listing all of the different campuses. Remove the campus names and mountains all together. Use simply the Colorado flag C and "Granite Ridge College".
Thanks for considering this brief!
Glen
Target Market(s)
Our college students love to ski and snowboard. In fact, one of our degrees is "Alpine Slope Commerce". Their ages are 18-22.
Industry/Entity Type
Events
Look and feel

```html
<!DOCTYPE html>
<html lang="en">
<head>
<meta charset="utf-8">
<title>We're at the 'Crest! – Welcome Week 2013</title>
<link href="https://fonts.googleapis.com/css2?family=Anton&family=Oswald:wght@300;400;500&family=Roboto+Condensed:wght@400;700&display=swap" rel="stylesheet">
<style>
  :root{
    --ink:#1c1e20;
    --panel:#232629;
    --photo-top:#0f2a36;
    --photo-mid:#1f4a5a;
    --photo-low:#3a6572;
    --letter-light:#c9d8dc;
    --letter-deep:#6f95a0;
    --white:#ffffff;
    --soft:#d7dadc;
    --navy:#1d3f86;
  }
  html,body{margin:0;padding:0;overflow:hidden;background:var(--ink);}
  .poster{position:relative;width:805px;height:1200px;overflow:hidden;background:var(--ink);}
  .hero{position:absolute;left:0;top:0;width:805px;height:470px;
    background:linear-gradient(180deg,var(--photo-top) 0%,var(--photo-mid) 55%,var(--photo-low) 85%,var(--ink) 100%);}
  .hero-title{position:absolute;left:0;top:0;width:805px;height:470px;}
  .kicker{font-family:'Anton',sans-serif;fill:var(--white);font-size:58px;letter-spacing:2px;}
  .headline{font-family:'Anton',sans-serif;font-size:330px;}
  .section-title{position:absolute;left:0;top:470px;width:805px;margin:0;text-align:center;
    font-family:'Oswald',sans-serif;font-weight:400;font-size:34px;letter-spacing:1px;color:var(--white);}
  .schedule{position:absolute;left:134px;top:536px;width:552px;height:470px;display:flex;gap:6px;}
  .day-column{flex:1;background:var(--panel);padding:14px 6px;box-sizing:border-box;
    font-family:'Roboto Condensed',sans-serif;font-size:10.5px;line-height:12.5px;color:var(--soft);text-align:center;}
  .event{margin:0 0 9px;}
  .event strong{color:var(--white);font-weight:700;}
  .note{margin-top:14px;color:var(--white);font-weight:700;}
  .brand{position:absolute;left:300px;top:1072px;width:205px;height:108px;background:var(--white);
    display:flex;align-items:center;justify-content:center;gap:10px;box-sizing:border-box;padding:0 12px;}
  .brand-mark{width:38px;height:38px;background:var(--navy);flex:none;}
  .brand-name{font-family:'Oswald',sans-serif;font-weight:500;font-size:19px;line-height:21px;color:var(--navy);text-transform:uppercase;}
</style>
</head>
<body>
<main class="poster">
  <div class="hero" role="img" aria-label="Photo of students in dark suits and sunglasses posing on the deck of a steamboat"></div>
  <svg class="hero-title" viewBox="0 0 805 470" aria-label="We're at the Crest">
    <defs>
      <linearGradient id="letterFill" x1="0" y1="0" x2="0" y2="1">
        <stop offset="0" stop-color="var(--letter-light)"/>
        <stop offset="1" stop-color="var(--letter-deep)"/>
      </linearGradient>
    </defs>
    <text class="kicker" x="402" y="88" text-anchor="middle">WE'RE AT THE</text>
    <text class="headline" x="54" y="440" textLength="712" lengthAdjust="spacingAndGlyphs" fill="url(#letterFill)">CREST</text>
  </svg>

  <h1 class="section-title">WELCOME WEEK 2013</h1>

  <section class="schedule">
    <div class="day-column">
      <p class="event"><strong>Thursday August 22</strong><br>Residence Hall Move-In<br>12:00pm-8:00pm<br>Dining Hall</p>
      <p class="event">Brunch<br>9:00am-1:00pm<br>Dining Hall</p>
      <p class="event">International Student Orientation<br>2:00pm<br>Room 221</p>
      <p class="event">Dinner<br>5:00pm-6:30pm<br>Dining Hall</p>
      <p class="event">Hot Springs Welcome Party<br>7:00pm-9:00pm<br>Valley Hot Springs</p>
      <p class="event"><strong>Friday August 23</strong><br>Breakfast<br>7:30am-9:00am<br>Dining Hall</p>
      <p class="event">Hike Pine Creek Falls<br>9:00am-12:00pm<br>Meet in Lobby at 8:45am</p>
      <p class="event">BBQ and Faculty Ice Cream Social<br>12:00pm-2:00pm<br>Quad Lawn</p>
      <p class="event">Bonfire Party<br>8:00pm-10:00pm<br>Campus Fire Pit</p>
    </div>
    <div class="day-column">
      <p class="event">Free Concert<br>7:00pm<br>Town Square</p>
      <p class="event"><strong>Saturday August 24</strong><br>Mountain Resort Welcome<br>10:00am-2:00pm<br>Gondola Plaza</p>
      <p class="event">Brunch<br>10:00am-1:00pm<br>Dining Hall</p>
      <p class="event">Street Fair Fun Run<br>3:00pm-5:00pm<br>Shuttle leaves at 2:30pm</p>
      <p class="event">Dinner<br>5:00pm-6:30pm<br>Dining Hall</p>
      <p class="event">Free Movie on the Mountain<br>8:00pm<br>Base Area Lawn</p>
      <p class="event"><strong>Sunday August 25</strong><br>Brunch<br>10:00am-1:00pm</p>
      <p class="event">Alpine Slope Volleyball<br>2:00pm-4:00pm<br>Recreation Field</p>
      <p class="event">Dinner<br>5:00pm-6:30pm<br>Dining Hall</p>
      <p class="event">Mandatory All-Hall Meeting<br>8:00pm<br>Auditorium</p>
    </div>
    <div class="day-column">
      <p class="event"><strong>Monday August 26</strong><br>Classes Begin<br>Student BBQ 11:30am<br>Quad Lawn</p>
      <p class="event">Being Home Sucks<br>8:00pm<br>Auditorium</p>
      <p class="event"><strong>Tuesday August 27</strong><br>Board Tournament Game<br>7:00pm-9:00pm<br>Student Lounge</p>
      <p class="event">Free Tacos<br>6:00pm-7:00pm<br>Dining Hall</p>
      <p class="event"><strong>Wednesday August 28</strong><br>Free Bowling<br>7:00pm<br>Town Lanes</p>
      <p class="event"><strong>Thursday August 29</strong><br>Comedy Night<br>8:00pm<br>Auditorium</p>
      <p class="event">Black Light Dodgeball<br>9:00pm<br>Gym</p>
      <p class="event"><strong>Friday August 30</strong><br>Late Night Climbing<br>9:00pm<br>Climbing Wall</p>
      <p class="note">ALL EVENTS ARE FREE<br>UNLESS OTHERWISE NOTED</p>
    </div>
  </section>

  <footer class="brand">
    <span class="brand-mark"></span>
    <span class="brand-name">Granite Ridge<br>College</span>
  </footer>
</main>
</body>
</html>
```